Simple Website Design for Law Office

I need a website design for our law office (Law Offices of Marcus Pellow) that is extremely simple, only including a landing page and perhaps a contact page (parallax scrolling).

Website should look similar to this one (template): https://www.brightfenwaystudio.com/

Design should be modern, simple, and inviting. There are a few assets like logo, stock photos/icons we would like added as well, and some language and contact info, but very basic stuff.

The name of the company is: Law Offices of Marcus Pellow

Target Market(s)

B2B corporate clients, users from Canada, UK, East Asia, and all potential users with immigration needs

Coding

Coded - Design and coding required

Number of Pages Required

2 page

Colors

Designer to choose colors to be used in the design.

Requirements
Must have
• Landing page, Contact Page
• Simple, elegant design with minimalist font
Nice to have
• Parallax scrolling, so one page and can scroll to contact us segment

```html
<!DOCTYPE html>
<html lang="en">
<head>
<meta charset="utf-8">
<title>Law Offices of Marcus Pellow</title>
<link href="https://fonts.googleapis.com/css2?family=Playfair+Display:wght@400;700&family=Poppins:wght@300;400;500;600&family=Rajdhani:wght@500&display=swap" rel="stylesheet">
<style>
:root{
  --gold:#c9ad4b;
  --dark:#25232b;
  --ink:#111;
  --text:#333;
  --field:#f5f5f5;
  --grey:#f8f8f8;
  --cream:#ece6da;
  --footer:#3a3745;
}
*{margin:0;padding:0;box-sizing:border-box}
html,body{width:1200px;height:2188px;overflow:hidden}
body{position:relative;font-family:"Poppins",sans-serif;color:var(--text);background:#fff}
.abs{position:absolute}
.serif{font-family:"Playfair Display",serif}

/* hero */
.hero{left:0;top:0;width:1200px;height:437px;background:radial-gradient(ellipse at 40% 60%,#34323a 0%,#25232b 60%,#1e1c23 100%)}
.hero-title{left:0;width:1200px;top:86px;text-align:center;color:#fff;font-size:42px;line-height:46px;letter-spacing:2px;font-weight:400}
.hero-rule{left:572px;top:201px;width:56px;height:2px;background:var(--gold)}
.hero-btn{left:489px;top:240px;width:222px;height:32px;background:var(--gold);color:#fff;font-size:10px;font-weight:600;letter-spacing:.3px;display:flex;align-items:center;justify-content:center}
.scroll-mouse{left:586px;top:363px}

/* about */
.about{left:0;top:437px;width:1200px;height:447px;background:linear-gradient(#ece6da 0%,#f6f3ee 40%,#fff 100%)}
.about-frame{left:234px;top:508px;width:325px;height:294px;background:var(--gold)}
.about-photo{left:246px;top:520px;width:325px;height:296px;background:linear-gradient(100deg,#2f3f5e 0%,#3c4d6d 38%,#c8cfd9 55%,#aab3c2 100%)}
.about-title{left:610px;top:536px;font-size:20px;font-weight:700;color:var(--ink)}
.about-copy{left:610px;top:577px;width:360px;font-size:9px;line-height:16.2px;color:#444}
.about-copy p+p{margin-top:16px}

/* practice */
.practice{left:0;top:884px;width:1200px;height:362px;background:var(--grey)}
.practice-title{left:0;width:1200px;top:930px;text-align:center;font-size:19px;font-weight:700;color:var(--ink)}
.practice-rule{left:578px;top:974px;width:44px;height:2px;background:var(--gold)}
.area{width:230px;height:80px}
.area-icon{position:absolute;left:0;top:0;width:51px;height:51px}
.area-name{position:absolute;left:66px;top:0;font-family:"Playfair Display",serif;font-size:16px;color:var(--ink);white-space:nowrap}
.area-text{position:absolute;left:66px;top:25px;width:160px;font-size:9px;line-height:15px;color:#444}

/* contact */
.contact-kicker{left:0;width:1190px;top:1300px;text-align:center;font-size:25px;font-weight:300;color:var(--ink)}
.contact-title{left:0;width:1190px;top:1330px;text-align:center;font-size:38px;font-weight:500;color:var(--ink)}
.field{background:var(--field);border:1px solid #eee;font-size:8px;color:#888;padding:10px 7px}
.submit{left:565px;top:1639px;width:63px;height:28px;border-radius:14px;background:var(--gold);color:#fff;font-size:8px;font-weight:600;display:flex;align-items:center;justify-content:center}

/* footer */
.footer{left:0;top:1727px;width:1200px;height:461px;background:linear-gradient(90deg,#403c4b 0%,#3a3745 50%,#34313e 100%)}
.cta-kicker{left:222px;width:400px;top:1800px;text-align:center;color:#fff;font-size:28px;font-weight:300}
.cta-title{left:212px;width:420px;top:1828px;text-align:center;color:#fff;font-size:37px;font-weight:500;letter-spacing:.5px}
.cta-phone{left:222px;width:400px;top:1886px;text-align:center;color:#fff;font-family:"Rajdhani",sans-serif;font-size:27px;font-weight:500;letter-spacing:.5px}
.cta-line{left:222px;width:400px;text-align:center;color:#fff;font-size:11px}
.map{left:650px;top:1792px;width:319px;height:207px;background:linear-gradient(135deg,#f1efe9,#e8e6df);border:3px solid #fff;border-radius:3px}
.copyright{left:0;width:1200px;top:2066px;text-align:center;color:#fff;font-size:9px}
.social{top:2105px;width:24px;height:24px;border:1px solid #fff;border-radius:50%}
</style>
</head>
<body>

<section class="abs hero">
  <h1 class="abs hero-title serif">Law Offices of<br>Marcus Pellow</h1>
  <div class="abs hero-rule"></div>
  <div class="abs hero-btn">CONTACT US FOR A CONSULTATION</div>
  <svg class="abs scroll-mouse" width="19" height="30" viewBox="0 0 19 30"><rect x="1" y="1" width="17" height="28" rx="8.5" fill="none" stroke="#fff" stroke-width="1.5"/><circle cx="9.5" cy="8" r="1.6" fill="#fff"/></svg>
</section>

<section class="abs about">
</section>
<div class="abs about-frame"></div>
<div class="abs about-photo" role="img" aria-label="Photo of two businessmen shaking hands"></div>
<h2 class="abs about-title serif">About Us</h2>
<div class="abs about-copy">
  <p>Vestibulum consectetur lectus finibus arcu consectetur consectetur. Nunc mattis vel augue nec iaculis. Ut cursus ex sit amet nisl lacinia porttitor. Proin tempus nunc sed faucibus porttitor. Nam luctus, ipsum in malesuada bibendum, nulla orci dictum arcu, a tempor erat metus lacinia lorem. Fusce fringilla est ut felis convallis auctor. Nam condimentum diam in sem commodo, a hendrerit tortor hendrerit. Nunc condimentum mauris ut hendrerit scelerisque. Nam convallis vulputate augue ut facilisis. Mauris ac diam eu est vehicula sollicitudin. Vivamus sollicitudin dapibus laoreet. Aliquam feugiat ipsum et velit tincidunt, non feugiat dui eleifend.</p>
  <p>Aliquam facilisis orci odio, in posuere leo suscipit nec. Praesent luctus leo nibh. In sed sem at risus fermentum porta ut a diam. Nam at ante est. Morbi vitae tortor ut diam bibendum faucibus aliquet in mauris.</p>
</div>

<section class="abs practice"></section>
<h2 class="abs practice-title serif">Our Practice Areas</h2>
<div class="abs practice-rule"></div>

<div class="abs area" style="left:234px;top:1019px">
  <svg class="area-icon" viewBox="0 0 51 51"><circle cx="25.5" cy="25.5" r="24.5" fill="none" stroke="#c9ad4b"/><g fill="none" stroke="#c9ad4b" stroke-width="1"><circle cx="19" cy="20" r="4"/><circle cx="32" cy="20" r="4"/><path d="M12 34v-4a7 7 0 0 1 14 0v4M25 34v-4a7 7 0 0 1 14 0v4"/></g></svg>
  <div class="area-name">Family Law</div>
  <div class="area-text">Lorem ipsum dolor sit amet, consectetur adipiscing elit. Cras a neque suscipit, tristique.</div>
</div>
<div class="abs area" style="left:484px;top:1019px">
  <svg class="area-icon" viewBox="0 0 51 51"><circle cx="25.5" cy="25.5" r="24.5" fill="none" stroke="#c9ad4b"/><g fill="none" stroke="#c9ad4b" stroke-width="1"><circle cx="26" cy="17" r="4"/><path d="M20 36v-9a6 6 0 0 1 12 0v9M21 30h-3v5"/></g></svg>
  <div class="area-name">Personal Injury</div>
  <div class="area-text">Lorem ipsum dolor sit amet, consectetur adipiscing elit. Cras a neque suscipit, tristique.</div>
</div>
<div class="abs area" style="left:734px;top:1019px">
  <svg class="area-icon" viewBox="0 0 51 51"><circle cx="25.5" cy="25.5" r="24.5" fill="none" stroke="#c9ad4b"/><g fill="none" stroke="#c9ad4b" stroke-width="1"><rect x="15" y="14" width="21" height="23"/><path d="M19 14v23M23 14v23M28 14v23M32 14v23M13 14h25M13 37h25"/></g></svg>
  <div class="area-name">Criminal Law</div>
  <div class="area-text">Lorem ipsum dolor sit amet, consectetur adipiscing elit. Cras a neque suscipit, tristique.</div>
</div>
<div class="abs area" style="left:234px;top:1120px">
  <svg class="area-icon" viewBox="0 0 51 51"><circle cx="25.5" cy="25.5" r="24.5" fill="none" stroke="#c9ad4b"/><g fill="none" stroke="#c9ad4b" stroke-width="1"><path d="M13 17h12v18H13zM25 17h12v18H25z"/><path d="M16 22h6M16 26h6M16 30h6M28 22h6M28 26h6M28 30h6"/></g></svg>
  <div class="area-name">Education Law</div>
  <div class="area-text">Lorem ipsum dolor sit amet, consectetur adipiscing elit. Cras a neque suscipit, tristique.</div>
</div>
<div class="abs area" style="left:484px;top:1120px">
  <svg class="area-icon" viewBox="0 0 51 51"><circle cx="25.5" cy="25.5" r="24.5" fill="none" stroke="#c9ad4b"/><g fill="none" stroke="#c9ad4b" stroke-width="1"><rect x="21" y="13" width="11" height="24"/><rect x="14" y="22" width="7" height="15"/><rect x="32" y="20" width="6" height="17"/><path d="M24 17h5M24 21h5M24 25h5M24 29h5"/></g></svg>
  <div class="area-name">Real Estate Law</div>
  <div class="area-text">Lorem ipsum dolor sit amet, consectetur adipiscing elit. Cras a neque suscipit, tristique.</div>
</div>
<div class="abs area" style="left:734px;top:1120px">
  <svg class="area-icon" viewBox="0 0 51 51"><circle cx="25.5" cy="25.5" r="24.5" fill="none" stroke="#c9ad4b"/><g fill="none" stroke="#c9ad4b" stroke-width="1"><rect x="13" y="19" width="25" height="15" rx="1.5"/><path d="M21 19v-3h9v3M13 25h25"/><rect x="24" y="23" width="3" height="4"/></g></svg>
  <div class="area-name">Business Law</div>
  <div class="area-text">Lorem ipsum dolor sit amet, consectetur adipiscing elit. Cras a neque suscipit, tristique.</div>
</div>

<section>
  <div class="abs contact-kicker">Get In Touch</div>
  <h2 class="abs contact-title">Contact Us</h2>
  <div class="abs field" style="left:349px;top:1405px;width:497px;height:32px">Your Name</div>
  <div class="abs field" style="left:349px;top:1449px;width:247px;height:32px">Email Address</div>
  <div class="abs field" style="left:599px;top:1449px;width:247px;height:32px">Phone Number</div>
  <div class="abs field" style="left:349px;top:1494px;width:497px;height:121px">Message</div>
  <div class="abs submit">SUBMIT</div>
</section>

<footer class="abs footer" role="img" aria-label="Dim photo of a columned courthouse facade"></footer>
<div class="abs cta-kicker">Have More Questions?</div>
<div class="abs cta-title">CONTACT US TODAY</div>
<div class="abs cta-phone">+1.416.555.0187</div>
<div class="abs cta-line" style="top:1925px">info@marcuspellow.com</div>
<div class="abs cta-line" style="top:1952px">54, Street Name, Country</div>
<div class="abs map" role="img" aria-label="Road map showing the office location"></div>
<svg class="abs" style="left:799px;top:1885px" width="14" height="20" viewBox="0 0 14 20"><path d="M7 0a7 7 0 0 1 7 7c0 5-7 13-7 13S0 12 0 7a7 7 0 0 1 7-7z" fill="#e11"/><circle cx="7" cy="7" r="2.5" fill="#fff"/></svg>
<div class="abs copyright">Copyright © 2019 marcuspellow. All Rights Reserved.</div>
<div class="abs social" style="left:541px"></div>
<div class="abs social" style="left:572px"></div>
<div class="abs social" style="left:604px"></div>
<div class="abs social" style="left:636px"></div>

</body>
</html>
```